For Creative Minds: A Simple Clean Book Cover that Stands Out

This will be a christian book teaching christians about divine healing. It is part of a series called "Morning Step Collection". I want the book cover to communicate the idea of healing, and specifically heavenly healing from God. These are some of the specifications below

1. General
Book to be published on print harbor platform
Dimensions: 6 x 9 inches, Paperback
Number of words: Estimated to be about 60,000 words.
Please use Indesign for design and submit the final Indesign source files along with the final design.

2. Cover image.
Image can be either human or any object that can communicate the idea above. No human faces to show up prominently.
High quality image is highly solicited.

3. Title:
" Forty Evenings Toward Lasting Renewal Within Your Soul"

3. Author name
Preferably should appear below. Open to creative ideas with titles that are better placed above.

Author's Name: Duncan Ferrow

3. Layout
Should not be too busy.
Simple and clean layout appeals more to me.

4. Series name
AS noted above, this book will be part of a series called " Morning Step Collection". I want this series name to appear somewhere in the cover and to have a simple but unique design that will be used for all subsequent titles. The Title of the book should have the emphasis.

I have attached a sample cover for one of my monthly devotional books which I choose from a contest.

ABOUT THE AUTHOR
Duncan Ferrow represents the blessed combination of Physician and Minister, bringing healing not only to the physical body but to the spiritual heart. He currently works as the Director of the Hospital Medicine Program at the Bellhaven County Care Campus in Iowa, USA. He is the Founder of Lantern & Vine Fellowship, a teaching ministry that seeks to bring believers into the fullness of grace — the glory of God — through conferences, seminars and books.

One of his notable quotes is “The Word of God is the most potent and efficient remedy for all the ailments of humanity.” This clearly portrays his experience with the Word as a Physician who is familiar with the powers, both natural and supernatural, to mend broken human beings. 

He currently lives in Iowa, USA with his wife, Lu Tessin, and daughter, Rosalind. You can reach out to Patrick using the contact information listed below.

BLURB
As a Physician and Minister, I have seen the power of modern medicine to bring about healing in the body and mind as well as the operation of the power of God to produce amazing medical results. However, many people are just not aware of the reality of divine healing. To some, it is a myth, belief or some "faith talk" in the heart. Medical miracles are real and we should take full advantage of it. As much as a love being a physician and treat patients in the hospital, I have come to see both its amazing successes and many limitations.

Industry/Entity Type

Christian

Font styles to use
Serif

Colors

Designer to choose colors to be used in the design.

Requirements
Should not have
• Too stylistic fonts

```html
<!DOCTYPE html>
<html lang="en">
<head>
<meta charset="utf-8">
<title>Forty Evenings Toward Lasting Renewal Within Your Soul — Duncan Ferrow</title>
<link rel="stylesheet" href="https://fonts.googleapis.com/css2?family=Cinzel:wght@400;500&display=swap">
<style>
  :root {
    --page-bg: #ffffff;
    --night-deep: #0b0c3a;
    --night-mid: #1d2080;
    --glow-violet: #5a5fd6;
    --glow-light: #dfe1ff;
    --title-ink: #ffffff;
    --series-ink: #c9ccff;
    --band-bg: #141653;
    --band-ink: #f2f2ff;
  }
  * { margin: 0; padding: 0; box-sizing: border-box; }
  html, body {
    width: 1200px;
    height: 1200px;
    overflow: hidden;
    background: var(--page-bg);
  }
  .canvas {
    position: relative;
    width: 1200px;
    height: 1200px;
  }
  .book-cover {
    position: absolute;
    left: 227px;
    top: 40px;
    width: 747px;
    height: 1120px;
    overflow: hidden;
    background: linear-gradient(180deg, var(--night-deep) 0%, #15176a 30%, var(--night-mid) 60%, #262a94 100%);
    font-family: "Cinzel", "Times New Roman", serif;
    color: var(--title-ink);
  }
  .cover-art {
    position: absolute;
    inset: 0;
    background:
      radial-gradient(ellipse 36% 11% at 50% 73%, rgba(245,246,255,0.95) 0%, rgba(200,204,255,0.8) 45%, rgba(120,126,230,0) 100%),
      radial-gradient(ellipse 44% 20% at 50% 70%, rgba(190,194,255,0.75) 0%, rgba(110,116,226,0.5) 55%, rgba(90,95,214,0) 100%),
      radial-gradient(ellipse 30% 30% at 50% 45%, rgba(205,208,255,0.6) 0%, rgba(120,125,230,0.4) 50%, rgba(90,95,214,0) 100%),
      radial-gradient(ellipse 48% 52% at 50% 52%, rgba(100,106,224,0.55) 0%, rgba(70,75,200,0.25) 60%, rgba(70,75,200,0) 100%),
      linear-gradient(180deg, rgba(11,12,58,0) 0%, rgba(11,12,58,0) 76%, rgba(120,126,224,0.55) 82%, rgba(70,76,190,0.6) 90%, rgba(40,44,140,0.85) 100%);
  }
  .series-mark {
    position: absolute;
    top: 20px;
    left: 0;
    width: 100%;
    display: flex;
    align-items: center;
    justify-content: center;
    gap: 14px;
    font-size: 17px;
    letter-spacing: 4px;
    color: var(--series-ink);
  }
  .series-mark::before,
  .series-mark::after {
    content: "";
    width: 60px;
    height: 1px;
    background: var(--series-ink);
  }
  .cover-title {
    position: absolute;
    top: 58px;
    left: 0;
    width: 100%;
    text-align: center;
    font-weight: 400;
  }
  .title-lead {
    display: block;
    font-weight: 400;
    font-size: 86px;
    line-height: 1.05;
    letter-spacing: 1px;
  }
  .title-rest {
    display: block;
    margin-top: 16px;
    font-weight: 400;
    font-size: 40px;
    line-height: 1.22;
    letter-spacing: 0.5px;
  }
  .author-band {
    position: absolute;
    left: 122px;
    bottom: 0;
    width: 492px;
    height: 98px;
    background: var(--band-bg);
    display: flex;
    align-items: center;
    justify-content: center;
  }
  .author-name {
    font-size: 48px;
    font-weight: 400;
    color: var(--band-ink);
    letter-spacing: 1px;
    white-space: nowrap;
  }
</style>
</head>
<body>
  <div class="canvas">
    <div class="book-cover">
      <div class="cover-art" role="img" aria-label="Glowing white lotus flower on still water, with a column of sparkling stars rising from it against a deep blue night sky"></div>
      <p class="series-mark">Morning Step Collection</p>
      <h1 class="cover-title">
        <span class="title-lead">Forty Evenings</span>
        <span class="title-rest">Toward Lasting Renewal<br>Within Your Soul</span>
      </h1>
      <div class="author-band">
        <p class="author-name">Duncan Ferrow</p>
      </div>
    </div>
  </div>
</body>
</html>
```